Letterhead Design for Corvane Communications

We are a Telecommunications Company, We wanting to get our Letterhead sorted as the one we have now looks Dull, It be used across our different databases we use but also mainly in Word , I have attached our Logo for you also, our website is corvane-example.com.au

We would only like to show our postal Address which is PO Box 8142 Tilford Cove NSW 2497

and we need to show our ABN Number Which we would be ABN: 61 804 327 918

Target Market(s)

Looks Stunning for our Proposals and General Usage

Industry/Entity Type

Telecommunications

Requirements
Must have
• Our Postal Address Only and Our ABN Number
Should not have
• Not listing our Actual Address

```html
<!DOCTYPE html>
<html lang="en">
<head>
<meta charset="utf-8">
<title>Corvane Communications Letterhead</title>
<link rel="stylesheet" href="https://fonts.googleapis.com/css2?family=Montserrat:wght@400;600;700&family=Questrial&family=Open+Sans:wght@600&family=Roboto:wght@400&display=swap">
<style>
  :root {
    --orange: #ef6b22;
    --green: #3fae49;
    --text-grey: #8c8c8c;
    --label-grey: #7d7d7d;
    --page-bg: #e9e9e9;
    --paper: #ffffff;
  }
  * { margin: 0; padding: 0; box-sizing: border-box; }
  html, body { width: 1051px; height: 1200px; overflow: hidden; background: var(--page-bg); }
  .letterhead {
    position: absolute; left: 112px; top: 20px;
    width: 827px; height: 1160px;
    background: var(--paper);
    box-shadow: 0 2px 10px rgba(0,0,0,0.15);
    font-family: "Montserrat", sans-serif;
    color: var(--text-grey);
  }
  .brand { position: absolute; left: 34px; top: 45px; display: flex; align-items: center; gap: 10px; }
  .brand-dot { width: 56px; height: 56px; border-radius: 50%; background: var(--orange); }
  .brand-name { font-family: "Montserrat", sans-serif; font-weight: 700; font-size: 22px; letter-spacing: 2px; color: var(--orange); line-height: 1.1; }
  .office-address { position: absolute; right: 58px; top: 43px; text-align: right; font-style: normal; font-size: 13.5px; line-height: 19px; color: var(--label-grey); }
  .office-abn { display: block; margin-top: 2px; }
  .office-pin { position: absolute; right: 37px; top: 44px; width: 16px; height: 20px; }
  .recipient { position: absolute; left: 38px; top: 254px; }
  .recipient-name { font-weight: 700; font-size: 27px; color: var(--orange); letter-spacing: 0.3px; margin-bottom: 6px; }
  .recipient-line { font-size: 14px; line-height: 27px; color: var(--text-grey); }
  .recipient-address { font-size: 14px; line-height: 20px; }
  .letter-date { position: absolute; right: 38px; top: 359px; font-family: "Open Sans", sans-serif; font-weight: 600; font-size: 16px; color: var(--label-grey); }
  .letter-body { position: absolute; left: 34px; right: 38px; top: 416px; font-family: "Questrial", sans-serif; font-size: 16.4px; line-height: 19.1px; text-align: justify; hyphens: auto; color: var(--text-grey); }
  .letter-body p + p { margin-top: 19px; }
  .letter-body p.spaced { margin-top: 38px; }
  .signatory-title { position: absolute; left: 61px; top: 800px; font-family: "Questrial", sans-serif; font-size: 21px; color: var(--label-grey); }
  .signature { position: absolute; left: 80px; top: 849px; width: 150px; height: 95px; background: linear-gradient(135deg, #f4f4f4, #e6e6e6); }
  .contact-bar { position: absolute; left: 0; right: 0; top: 1059px; display: flex; justify-content: center; gap: 22px; font-family: "Roboto", sans-serif; font-size: 16px; color: var(--label-grey); }
  .contact-item { display: flex; align-items: center; gap: 6px; }
  .contact-icon { width: 20px; height: 20px; }
  .footer-rule { position: absolute; left: 0; top: 1113px; width: 827px; height: 13px; }
  .fill-green { fill: var(--green); }
  .fill-orange { fill: var(--orange); }
  .stroke-green { stroke: var(--green); }
</style>
</head>
<body>
<main class="letterhead">
  <header>
    <div class="brand">
      <span class="brand-dot"></span>
      <span class="brand-name">CORVANE</span>
    </div>
    <address class="office-address">PO Box 8142<br>Tilford Cove<br>NSW 2497<span class="office-abn">ABN: 61 804 327 918</span></address>
    <svg class="office-pin" viewBox="0 0 16 20" aria-hidden="true">
      <path class="fill-green" d="M8 0a6.5 6.5 0 0 0-6.5 6.5C1.5 11 8 16 8 16s6.5-5 6.5-9.5A6.5 6.5 0 0 0 8 0z"/>
      <circle cx="8" cy="6.5" r="2.5" fill="#fff"/>
      <ellipse class="stroke-green" cx="8" cy="18" rx="5" ry="1.5" fill="none" stroke-width="1.2"/>
    </svg>
  </header>

  <section class="recipient">
    <h1 class="recipient-name">MARA ELLISON</h1>
    <div class="recipient-line">0123-456-789</div>
    <div class="recipient-line">info@youremailaddress.com</div>
    <div class="recipient-line recipient-address">1234 City Your Ln. Suite<br>123 Dallas, TX 0000</div>
  </section>

  <div class="letter-date">12 December, 2023</div>

  <article class="letter-body">
    <p>Lorem ipsum dolor sit amet, consectetuer adipiscing elit, sed diam nonummy nibh euismod tincidunt ut laoreet dolore magna aliquam erat volutpat. Ut wisi enim ad minim veniam, quis nostrud exerci tation ullamcorper suscipit lobortis nisl ut aliquip ex ea commodo consequat. Duis autem vel eum iriure dolor in hendrerit in vulputate velit esse molestie consequat, vel illum dolore eu feugiat nulla facilisis at vero eros et accumsan et iusto odio dignissim qui blandit praesent luptatum zzril delenit augue duis dolore te feugait nulla facilisi.</p>
    <p>Lorem ipsum dolor sit amet, cons ectetuer adipiscing elit, sed diam nonummy nibh euismod tincidunt ut laoreet dolore magna aliquam erat volutpat. Ut wisi enim ad minim veniam, quis nostrud exerci tation ullamcorper suscipit lobortis nisl ut aliquip ex ea commodo consequat.<br>Lorem ipsum dolor sit amet, consectetuer adipiscing elit, sed diam nonummy nibh euismod tincidunt ut laoreet dolore magna aliquam erat</p>
    <p class="spaced">Lorem ipsum dolor sit amet, cons ectetuer adipiscing elit, sed diam nonummy nibh euismod tincidunt ut laoreet dolore magna aliquam erat volutpat. Ut wisi enim ad minim veniam, quis nostrud exerci tation ullamcorper suscipit lobortis nisl ut aliquip ex ea commodo consequat. Lorem ipsum dolor sit zamet, consectetuer adipiscing elit, sed diam nonummy nibh euismod tincidunt.</p>
  </article>

  <div class="signatory-title">Managing Director</div>
  <div class="signature" role="img" aria-label="Handwritten signature of the Managing Director"></div>

  <footer>
    <div class="contact-bar">
      <span class="contact-item">
        <svg class="contact-icon" viewBox="0 0 20 20" aria-hidden="true"><rect class="fill-green" width="20" height="20" rx="2"/><path d="M6.2 4.5l2 2.3-1.2 1.6c.8 1.7 2 2.9 3.7 3.7l1.6-1.2 2.3 2-1.3 2.1C9 14.6 5.4 11 4.1 5.8z" fill="#fff"/></svg>
        1800 555 014
      </span>
      <span class="contact-item">
        <svg class="contact-icon" viewBox="0 0 20 20" aria-hidden="true"><rect class="fill-green" width="20" height="20" rx="2"/><rect x="4" y="6" width="12" height="8.5" fill="none" stroke="#fff" stroke-width="1.3"/><path d="M4 6l6 5 6-5M4 14.5l4.5-4M16 14.5l-4.5-4" fill="none" stroke="#fff" stroke-width="1.1"/></svg>
        info@corvane-example.com.au
      </span>
      <span class="contact-item">
        <svg class="contact-icon" viewBox="0 0 20 20" aria-hidden="true"><rect class="fill-green" width="20" height="20" rx="2"/><path d="M6 4v11l3-2.6 2 4.3 1.8-.8-2-4.3 4-.3z" fill="#fff"/></svg>
        corvane-example.com.au
      </span>
    </div>
    <svg class="footer-rule" viewBox="0 0 827 13" aria-hidden="true">
      <line class="stroke-green" x1="395" y1="6.5" x2="827" y2="6.5" stroke-width="1"/>
      <polygon class="fill-orange" points="0,0 385,0 397,13 0,13"/>
    </svg>
  </footer>
</main>
</body>
</html>
```